Carpentry and Building Business Card

I'm looking for a business card that is minimalistic and that incorporates the theme of my Velmor logo.
On one side I'd like the VELMOR logo with my details on the other side.
Double sided with curved edges

Target Market(s)

Construction / renovation
Adults

Industry/Entity Type

Tradesman

Contact Information for Business Card

Logo on one side, details on the other

Colors

Designer to choose only greyscale colors for use in the design.

Requirements
Must have
• Nilo Petrakis
VELMOR CONSTRUCT
Carpentry & Building Services
0481236574
Velmorconstruct@brixmail.com
Lic No. 718263D
Nice to have
• Fb and insta icons. @velmorconstruct
Should not have
• No hammer or tool icons please.

No address line.

```html
<!DOCTYPE html>
<html lang="en">
<head>
<meta charset="utf-8">
<title>Velmor Construct – Business Card</title>
<link href="https://fonts.googleapis.com/css2?family=Montserrat:wght@400;500;700&display=swap" rel="stylesheet">
<style>
  :root {
    --backdrop: #dcdcdc;
    --card-dark-start: #1a1a1a;
    --card-dark-end: #343434;
    --card-light: #ffffff;
    --accent: #ee9a3a;
    --ink: #2b2b2b;
    --wordmark: #ffffff;
  }
  * { margin: 0; padding: 0; box-sizing: border-box; }
  html, body {
    width: 1200px;
    height: 549px;
    overflow: hidden;
    background: var(--backdrop);
    font-family: "Montserrat", sans-serif;
  }
  .canvas { position: relative; width: 1200px; height: 549px; }

  .card {
    position: absolute;
    top: 150px;
    width: 434px;
    height: 248px;
    border-radius: 17px;
    overflow: hidden;
  }
  .card--front {
    left: 128px;
    background: linear-gradient(110deg, var(--card-dark-start), var(--card-dark-end));
  }
  .card--back {
    left: 637px;
    background: var(--card-light);
    color: var(--ink);
  }

  /* Front: brand lockup */
  .brand-mark {
    position: absolute;
    left: 66px;
    top: 104px;
    width: 40px;
    height: 40px;
    border: 3px solid var(--accent);
  }
  .brand-name {
    position: absolute;
    left: 136px;
    top: 106px;
    font-size: 30px;
    font-weight: 500;
    letter-spacing: 12px;
    line-height: 1;
    color: var(--wordmark);
  }

  /* Back: details */
  .licence {
    position: absolute;
    right: 15px;
    top: 16px;
    font-size: 13px;
    line-height: 1;
  }
  .company {
    position: absolute;
    left: 30px;
    top: 46px;
    font-size: 22.5px;
    font-weight: 700;
    line-height: 1;
    color: var(--accent);
  }
  .tagline {
    position: absolute;
    left: 30px;
    top: 71px;
    font-size: 13.5px;
    line-height: 1;
  }
  .person {
    position: absolute;
    left: 30px;
    top: 112px;
    font-size: 20.5px;
    font-weight: 700;
    line-height: 1;
    color: var(--accent);
  }
  .contact-list {
    position: absolute;
    left: 30px;
    top: 143px;
    list-style: none;
  }
  .contact-item {
    display: flex;
    align-items: center;
    height: 17px;
    font-size: 12px;
    line-height: 1;
  }
  .contact-icon {
    width: 11px;
    height: 11px;
    margin-right: 7px;
    flex: none;
  }
  .contact-icon--plain {
    background: var(--accent);
    border-radius: 2px;
  }
</style>
</head>
<body>
<main class="canvas">
  <section class="card card--front" aria-label="Card front">
    <span class="brand-mark" aria-hidden="true"></span>
    <span class="brand-name">VELMOR.</span>
  </section>

  <section class="card card--back" aria-label="Card back">
    <p class="licence">Lic No. 718263D</p>
    <h1 class="company">VELMOR CONSTRUCT</h1>
    <p class="tagline">Carpentry &amp; Building Service</p>
    <h2 class="person">Nilo Petrakis</h2>
    <ul class="contact-list">
      <li class="contact-item">
        <svg class="contact-icon" viewBox="0 0 11 11" aria-hidden="true">
          <rect x="2" y="0.7" width="7" height="9.6" rx="1.4" fill="none" stroke="#ee9a3a" stroke-width="1.3"/>
          <line x1="4.5" y1="8.5" x2="6.5" y2="8.5" stroke="#ee9a3a" stroke-width="1"/>
        </svg>
        0481236574
      </li>
      <li class="contact-item">
        <svg class="contact-icon" viewBox="0 0 11 11" aria-hidden="true">
          <rect x="0.5" y="2" width="10" height="7" fill="#ee9a3a"/>
          <polyline points="0.5,2 5.5,6 10.5,2" fill="none" stroke="#ffffff" stroke-width="1"/>
        </svg>
        velmorconstruct@brixmail.com
      </li>
      <li class="contact-item">
        <span class="contact-icon contact-icon--plain" aria-hidden="true"></span>
        velmorconstruct
      </li>
      <li class="contact-item">
        <span class="contact-icon contact-icon--plain" aria-hidden="true"></span>
        velmorconstruct
      </li>
    </ul>
  </section>
</main>
</body>
</html>
```